I need a business Card Design for my practice , i am clinical herbalist. I am a herbalist specializing in Lyme disease, autism, autoimmune diseases, difficult to cure diseasesDifficult to cure diseases. In my innovative practice i link traditional medicine, herbs with science, immunologu ,pharmacology.

Industry/Entity Type

Business

Contact Information for Business Card

My company name : OSRODEK ZIELNIKA
My name : Piotr Weltak
Name of my profession : Fitoterapeuta
In Polish language Fitoterapeuta is Herbalist .

e-mail: piotrweltak@osrodekzielnika.com
www.osrodek-zielnika.pl
phone : 574 806 215
My company adress : Dąbrowa Sękowska 14 , 38-415 Mielnik
I dont have logo .

Requirements
Nice to have
• My company

```html
<!DOCTYPE html>
<html lang="pl">
<head>
<meta charset="UTF-8">
<title>Osrodek Zielnika – wizytówka</title>
<link href="https://fonts.googleapis.com/css2?family=Roboto+Condensed:wght@700&family=Roboto:wght@400;500;700&display=swap" rel="stylesheet">
<style>
  :root {
    --bg: #e4e6e3;
    --card: #ffffff;
    --ink: #2b2b2b;
    --green: #0aa14e;
    --green-dark: #2fae4a;
    --lime: #8cc63f;
    --rule: #9a9a9a;
  }
  * { margin: 0; padding: 0; box-sizing: border-box; }
  html, body { width: 1200px; height: 900px; overflow: hidden; }
  body {
    background: var(--bg);
    font-family: "Roboto", Arial, sans-serif;
    color: var(--ink);
    position: relative;
  }
  .card {
    position: absolute;
    width: 640px;
    height: 366px;
    background: var(--card);
    box-shadow: 0 6px 18px rgba(0,0,0,.18);
    overflow: hidden;
  }
  .card--front { left: 420px; top: 50px; }
  .card--back { left: 140px; top: 470px; }

  /* front */
  .front-mark {
    position: absolute;
    left: 285px; top: 62px;
    width: 150px; height: 150px;
    border-radius: 50%;
    background: var(--green);
    border: 5px solid var(--card);
    box-shadow: 0 0 0 4px var(--lime);
  }
  .front-name {
    position: absolute;
    left: 0; right: 0; top: 232px;
    text-align: center;
    font-family: "Roboto Condensed", Arial, sans-serif;
    font-weight: 700;
    font-size: 40px;
    letter-spacing: .5px;
    color: var(--ink);
  }
  .front-tagline {
    position: absolute;
    left: 0; right: 0; top: 284px;
    text-align: center;
    font-size: 17px;
    color: var(--lime);
  }

  /* back */
  .back-mark {
    position: absolute;
    left: 40px; top: 60px;
    width: 176px; height: 176px;
    border-radius: 50%;
    background: var(--green);
    border: 6px solid var(--card);
    box-shadow: 0 0 0 5px var(--lime);
  }
  .back-divider {
    position: absolute;
    left: 258px; top: 58px;
    width: 1px; height: 180px;
    background: var(--rule);
  }
  .back-details { position: absolute; left: 282px; top: 52px; }
  .company {
    font-family: "Roboto Condensed", Arial, sans-serif;
    font-weight: 700;
    font-size: 34px;
    line-height: 1.05;
    color: var(--ink);
  }
  .person { font-weight: 700; font-size: 22px; margin-top: 8px; }
  .role { font-weight: 500; font-size: 16px; color: var(--green); margin-bottom: 12px; }
  .contact { list-style: none; font-size: 16px; line-height: 1.55; }
  .contact li { display: flex; align-items: center; gap: 10px; }
  .contact svg { width: 15px; height: 15px; flex: none; }
  .address {
    position: absolute;
    left: 40px; bottom: 50px;
    font-size: 17px;
  }
  .band {
    position: absolute;
    left: 0; right: 0; bottom: 0;
    height: 22px;
    display: flex;
  }
  .band__dark { width: 42%; background: var(--green-dark); }
  .band__light { flex: 1; background: var(--lime); }
</style>
</head>
<body>

<section class="card card--front">
  <div class="front-mark" aria-hidden="true"></div>
  <h1 class="front-name">OSRODEK ZIELNIKA</h1>
  <p class="front-tagline">Borelioza, choroby autoimmunologiczne , autyzm</p>
</section>

<section class="card card--back">
  <div class="back-mark" aria-hidden="true"></div>
  <div class="back-divider"></div>
  <div class="back-details">
    <h2 class="company">OSRODEK ZIELNIKA</h2>
    <p class="person">Piotr Weltak</p>
    <p class="role">Fitoterapeuta</p>
    <ul class="contact">
      <li>
        <svg viewBox="0 0 16 16" aria-hidden="true"><path fill="#0aa14e" d="M3.6 1.2l2.3 2.6-1.2 1.9c.9 2 2.4 3.5 4.4 4.4l1.9-1.2 2.6 2.3-1.3 2.5C7.2 13.5 2.5 8.8 1.1 2.5z"/></svg>
        574 806 215
      </li>
      <li>
        <svg viewBox="0 0 16 16" aria-hidden="true"><rect x="1" y="3" width="14" height="10" fill="#0aa14e"/><path d="M1.5 3.5L8 9l6.5-5.5" stroke="#fff" stroke-width="1.3" fill="none"/></svg>
        piotrweltak@osrodekzielnika.com
      </li>
      <li>
        <svg viewBox="0 0 16 16" aria-hidden="true"><g fill="none" stroke="#0aa14e" stroke-width="1.3"><circle cx="8" cy="8" r="6.5"/><ellipse cx="8" cy="8" rx="3" ry="6.5"/><path d="M1.5 8h13M2.5 4.8h11M2.5 11.2h11"/></g></svg>
        www.osrodek-zielnika.pl
      </li>
    </ul>
  </div>
  <p class="address">Dąbrowa Sękowska 14 , 38-415 Mielnik</p>
  <div class="band"><span class="band__dark"></span><span class="band__light"></span></div>
</section>

</body>
</html>
```